Motor Vault Website - Part of the Brantley Group

A complimentary website is required for the launch of a 'Motor Vault' - a new service launched by industry renowned BRANTLEY. Motor Vault is an industry-first brand that designs and builds unique subterranean car parks for private residential homes in London and the influential counties within the UK. Please see here the direction of a new BRANTLEY Website - we would like Motor Vault to be complimentary and sit alongside BRANTLEY harmoniously - https://www.brantleyhomes.example/brantley-nu-staging Brantley have some images, but whilst more professional images are in production - we have also attached pixmora photos- named clearly as pixmora. **Attached files include JPEG, .eps of logo and Brantley library images and Pixmora Library Images - two versions of logo dependent on background colour. - Website needs to be sleek, chic and masculine.- Colour Palette - Grey/ Black/ White - Same visiual journey as Brantley website- Required areas within the sit include - About Us / Our Work / Contact Page

Target Market(s)

Luxury
Men

Number of Pages Required

2 page

Font styles to use
Sans Serif

Colors
e8e8e8
757575
1b1b1b
000000
9d9d9d
cbcbcb
f5f5f5

Requirements
Must have
• Complimentary of this site - https://www.brantleyhomes.example/brantley-nu-staging
Should not have
• Colour

```html
<!DOCTYPE html>
<html lang="en">
<head>
<meta charset="utf-8">
<title>Motor Vault</title>
<link href="https://fonts.googleapis.com/css2?family=Montserrat:wght@400;500;600;700&family=Open+Sans:wght@400;600&display=swap" rel="stylesheet">
<style>
:root{
  --white:#ffffff;
  --off:#f5f5f5;
  --light:#e8e8e8;
  --silver:#cbcbcb;
  --grey:#9d9d9d;
  --mid:#757575;
  --band:#6a6a6a;
  --dark:#1b1b1b;
  --black:#000000;
}
*{box-sizing:border-box;margin:0;padding:0}
html,body{width:1200px;height:3352px;overflow:hidden;background:var(--black)}
body{position:relative;font-family:'Open Sans',Arial,sans-serif;color:var(--white)}
.abs{position:absolute}
.heading{font-family:'Montserrat',Arial,sans-serif;font-weight:600;text-transform:uppercase;letter-spacing:.5px}
/* header */
.site-header{left:0;top:0;width:1200px;height:163px;background:linear-gradient(180deg,#5e5e5e,#4c4c4c)}
.brand{display:flex;align-items:center;gap:14px}
.brand-mark{width:34px;height:34px;background:var(--white)}
.brand-name{font-family:'Montserrat',Arial,sans-serif;font-weight:500;font-size:44px;letter-spacing:1px;color:var(--white);line-height:1}
.brand-tag{font-family:'Montserrat',Arial,sans-serif;font-size:9px;letter-spacing:.5px;color:var(--light);text-transform:uppercase}
.support{left:577px;top:33px;display:flex;gap:14px;align-items:center}
.support small{display:block;font-family:'Montserrat',Arial,sans-serif;font-size:15px;font-weight:600}
.support strong{display:block;font-family:'Montserrat',Arial,sans-serif;font-size:26px;font-weight:500;line-height:1.1}
.search{left:867px;top:33px;width:243px;height:43px;border-radius:22px;background:var(--white);display:flex;align-items:center;padding-left:14px;color:var(--mid);font-size:14px;gap:6px}
.search .go{position:absolute;right:6px;top:6px;width:31px;height:31px;border-radius:50%;background:var(--black)}
.nav{top:102px;left:525px;display:flex;gap:0;font-family:'Montserrat',Arial,sans-serif;font-size:16px}
.nav a{color:var(--white);text-decoration:none;position:absolute;white-space:nowrap}
.social-top{left:985px;top:104px;display:flex;gap:18px}
.dot{width:16px;height:16px;border-radius:50%;background:var(--white)}
/* photo fills */
.photo{position:absolute}
/* hero */
.hero-bg{left:0;top:163px;width:1200px;height:640px;background:radial-gradient(ellipse at 55% 30%,#6e6e6e 0%,#3a3a3a 40%,#141414 80%)}
.hero-box{left:282px;top:257px;width:634px;height:302px;background:rgba(0,0,0,.55);text-align:center}
.hero-box h1{font-size:32px;margin-top:60px}
.hero-box p{font-size:15px;line-height:31px;width:510px;margin:6px auto 0;text-align:justify;text-align-last:center}
.btn{display:inline-flex;align-items:center;gap:8px;background:var(--mid);color:var(--white);font-family:'Montserrat',Arial,sans-serif;font-weight:600;font-size:15px;text-transform:uppercase;justify-content:center}
.hero-box .btn{position:absolute;left:241px;top:210px;width:156px;height:45px}
/* about */
.about-bg{left:0;top:793px;width:1200px;height:650px;background:linear-gradient(180deg,#0a0a0a,#1b1b1b 60%,#0d0d0d)}
.about-photo{left:112px;top:894px;width:496px;height:353px;background:radial-gradient(ellipse at 50% 60%,#d8d8d8 0%,#7a7a7a 30%,#2a2a2a 75%)}
.about-copy{left:644px;top:905px;width:464px}
.about-copy h2{font-size:32px}
.about-copy p{font-size:15px;line-height:31.7px;margin-top:6px;text-align:justify}
.about-copy .btn{margin-top:20px;width:158px;height:43px}
/* work */
.work-bg{left:0;top:1400px;width:1200px;height:780px;background:radial-gradient(ellipse at 50% 40%,#3a3a3a,#1b1b1b 55%,#0a0a0a)}
.section-head{left:0;width:1200px;text-align:center}
.section-head h2{font-size:32px}
.section-head p{font-size:15px;line-height:31px;width:900px;margin:8px auto 0}
.tile{border:1px solid var(--mid);padding:7px}
.tile div{width:100%;height:100%}
/* contact */
.contact-bg{left:0;top:2150px;width:1200px;height:700px;background:linear-gradient(180deg,#151515,#232323 50%,#101010)}
.field{border:2px solid var(--light);height:38px;display:flex;align-items:center;gap:8px;padding-left:12px;font-size:12px;color:var(--white)}
.submit{left:518px;top:2664px;width:161px;height:47px}
/* footer */
.footer-bg{left:0;top:2860px;width:1200px;height:492px;background:linear-gradient(180deg,#2a2a2a,#161616 70%,#0a0a0a)}
.contact-item{width:300px;text-align:center;font-family:'Montserrat',Arial,sans-serif;font-weight:600;font-size:16px;line-height:29px}
.footer-links{left:0;top:3274px;width:1200px;text-align:center;font-family:'Montserrat',Arial,sans-serif;font-weight:600;font-size:14px}
.footer-links span{margin:0 10px}
.copyright{left:0;top:3313px;width:1200px;text-align:center;font-size:13px;color:var(--light)}
.ring{width:30px;height:30px;border:2px solid var(--white);border-radius:50%}
</style>
</head>
<body>

<!-- hero photo -->
<div class="photo abs hero-bg" role="img" aria-label="Underground car park construction site in black and white"></div>

<header class="site-header abs">
  <div class="brand abs" style="left:103px;top:50px">
    <span class="brand-mark"></span>
    <div>
      <div class="brand-name">MOTOR VAULT</div>
      <div class="brand-tag" style="text-align:right;margin-top:3px">Part of the Brantley Group</div>
    </div>
  </div>
  <div class="support abs">
    <svg width="40" height="40" viewBox="0 0 40 40"><circle cx="20" cy="20" r="18" fill="none" stroke="#fff" stroke-width="2.5"/><path d="M13 12c1-1 3-1 4 0l2 3c.6 1 .3 2-.5 2.6l-1.2.9c1 2.5 2.7 4.2 5.2 5.2l.9-1.2c.6-.8 1.6-1.1 2.6-.5l3 2c1 1 1 3 0 4l-1 1c-6 2-17-9-15-15z" fill="#fff"/></svg>
    <div><small>Support Call us</small><strong>0330 555 0192</strong></div>
  </div>
  <div class="search abs">
    <svg width="14" height="14" viewBox="0 0 14 14"><circle cx="6" cy="6" r="4.5" fill="none" stroke="#555" stroke-width="1.6"/><path d="M9.5 9.5 13 13" stroke="#555" stroke-width="1.6"/></svg>
    Search
    <span class="go"><svg width="31" height="31" viewBox="0 0 31 31"><circle cx="14" cy="14" r="5" fill="none" stroke="#fff" stroke-width="2"/><path d="M18 18l4 4" stroke="#fff" stroke-width="2"/></svg></span>
  </div>
  <nav class="nav abs" style="left:0;width:1200px">
    <a style="left:525px">Welcome</a>
    <a style="left:646px">About Us</a>
    <a style="left:764px">Our Work</a>
    <a style="left:885px">Contact</a>
  </nav>
  <div class="social-top abs"><span class="dot"></span><span class="dot"></span><span class="dot"></span><span class="dot"></span></div>
</header>

<section class="hero">
  <svg class="abs" style="left:282px;top:257px" width="634" height="302" viewBox="0 0 634 302">
    <path d="M5 110V5h110" fill="none" stroke="#fff" stroke-width="10"/>
    <path d="M629 192v105H519" fill="none" stroke="#fff" stroke-width="10"/>
  </svg>
  <div class="hero-box abs">
    <h1 class="heading">Welcome to Motor Vault</h1>
    <p>Sed ut perspiciatis unde omnis iste natus error sit voluptatem accusantium doloremque laudantium, totam rem aperiam, eaque ipsa quae ab illo inventore veritatis sunt explicabo.</p>
    <a class="btn">Read More
      <svg width="14" height="14" viewBox="0 0 14 14"><path d="M1 7h10M7 2l5 5-5 5" fill="none" stroke="#fff" stroke-width="2.4"/></svg></a>
  </div>
</section>

<!-- about -->
<div class="abs about-bg"></div>
<svg class="abs" style="left:0;top:730px" width="1200" height="110" viewBox="0 0 1200 110"><polygon points="0,110 0,60 1200,20 1200,110" fill="#0a0a0a"/><polygon points="0,62 1200,22 1200,42 0,90" fill="#8a8a8a" opacity=".55"/></svg>
<section class="about">
  <svg class="abs" style="left:92px;top:874px" width="536" height="393" viewBox="0 0 536 393">
    <path d="M0 0h140v18H18v122H0z" fill="#757575"/>
    <path d="M536 393H396v-18h122V253h18z" fill="#757575"/>
  </svg>
  <div class="photo abs about-photo" role="img" aria-label="Empty concrete underground garage with pillars"></div>
  <div class="about-copy abs">
    <h2 class="heading">About Us</h2>
    <p>Sed ut perspiciatis unde omnis iste natus error sit voluptatem accusantium doloremque laudantium, totam rem aperiam, eaque ipsa quae ab illo inventore veritatis et quasi architecto beatae vitae dicta sunt explicabo. Nemo enim ipsam voluptatem quia voluptas sit aspernatur aut odit aut fugit, sed quia consequuntur magni dolores eos qui ratione voluptatem sequi nesciunt. Neque porro quisquam est, qui dolorem</p>
    <a class="btn">Read More
      <svg width="14" height="14" viewBox="0 0 14 14"><path d="M1 7h10M7 2l5 5-5 5" fill="none" stroke="#fff" stroke-width="2.4"/></svg></a>
  </div>
</section>

<!-- our work -->
<div class="photo abs work-bg" role="img" aria-label="Dim excavation site backdrop"></div>
<svg class="abs" style="left:0;top:1345px" width="1200" height="100" viewBox="0 0 1200 100"><polygon points="0,0 160,80 1200,90 1200,100 0,100" fill="#101010"/><polygon points="0,0 220,70 0,90" fill="#8a8a8a"/></svg>
<section class="work">
  <div class="section-head abs" style="top:1466px">
    <h2 class="heading">Our Work</h2>
    <p>Sed ut perspiciatis unde omnis iste natus error sit voluptatem accusantium doloremque laudantium, totam rem aperiam, eaque ipsa quae ab illo inventore veritatis et quasi architecto beatae vitae dicta sunt explicabo.</p>
  </div>
  <div class="tile abs" style="left:89px;top:1607px;width:331px;height:230px"><div role="img" aria-label="Excavator inside a basement dig" style="background:linear-gradient(160deg,#bdbdbd,#555 60%,#2a2a2a)"></div></div>
  <div class="tile abs" style="left:434px;top:1607px;width:330px;height:230px"><div role="img" aria-label="Steel support frame overhead" style="background:linear-gradient(135deg,#e0e0e0,#6a6a6a 50%,#202020)"></div></div>
  <div class="tile abs" style="left:778px;top:1607px;width:332px;height:230px"><div role="img" aria-label="Machinery in an underground shaft" style="background:radial-gradient(ellipse at 60% 50%,#9a9a9a,#2e2e2e 70%)"></div></div>
  <div class="tile abs" style="left:89px;top:1855px;width:331px;height:228px"><div role="img" aria-label="Concrete vault with ceiling beams" style="background:linear-gradient(120deg,#f0f0f0,#8a8a8a 40%,#1e1e1e)"></div></div>
  <div class="tile abs" style="left:434px;top:1855px;width:330px;height:228px"><div role="img" aria-label="Scaffolding lit by light shaft" style="background:radial-gradient(ellipse at 45% 40%,#e8e8e8,#4a4a4a 45%,#121212)"></div></div>
  <div class="tile abs" style="left:778px;top:1855px;width:332px;height:228px"><div role="img" aria-label="Finished garage wall under strip lights" style="background:linear-gradient(180deg,#2a2a2a,#5a5a5a 55%,#cfcfcf 85%,#3a3a3a)"></div></div>
</section>

<!-- contact -->
<div class="photo abs contact-bg" role="img" aria-label="Dark construction site backdrop"></div>
<svg class="abs" style="left:0;top:2128px" width="1200" height="100" viewBox="0 0 1200 100"><polygon points="0,100 1000,30 1200,0 1200,100" fill="#151515"/><polygon points="760,40 1200,0 1200,60" fill="#8a8a8a"/></svg>
<section class="contact">
  <div class="section-head abs" style="top:2293px">
    <h2 class="heading">Get in Touch</h2>
    <p style="width:860px">At vero eos et accusamus et iusto odio dignissimos ducimus qui blanditiis praesentium voluptatum deleniti atque corrupti quos dolores et quas molestias excepturi sint occaecati cupiditate non provident</p>
  </div>
  <div class="field abs" style="left:163px;top:2438px;width:427px"><svg width="11" height="11" viewBox="0 0 11 11"><circle cx="5.5" cy="3" r="2.6" fill="#fff"/><path d="M0 11c0-4 11-4 11 0z" fill="#fff"/></svg>First Name</div>
  <div class="field abs" style="left:610px;top:2438px;width:427px"><svg width="11" height="11" viewBox="0 0 11 11"><circle cx="5.5" cy="3" r="2.6" fill="#fff"/><path d="M0 11c0-4 11-4 11 0z" fill="#fff"/></svg>Last Name</div>
  <div class="field abs" style="left:163px;top:2492px;width:427px"><svg width="10" height="11" viewBox="0 0 10 11"><rect width="10" height="11" fill="#fff"/></svg>Company</div>
  <div class="field abs" style="left:163px;top:2545px;width:427px"><svg width="12" height="9" viewBox="0 0 12 9"><rect width="12" height="9" fill="#fff"/><path d="M0 0l6 5 6-5" fill="none" stroke="#000"/></svg>Email Address</div>
  <div class="field abs" style="left:163px;top:2599px;width:427px"><svg width="11" height="11" viewBox="0 0 11 11"><path d="M1 1c1-1 2-1 3 0l1 2-1 1.3c.8 1.5 1.7 2.4 3.2 3.2L8.5 6.5l2 1c1 1 0 2.5-1 3C5 11 0 6 1 1z" fill="#fff"/></svg>Phone Number</div>
  <div class="field abs" style="left:610px;top:2492px;width:427px;height:147px;align-items:flex-start;padding-top:10px"><svg width="12" height="10" viewBox="0 0 12 10"><ellipse cx="6" cy="4.5" rx="6" ry="4.5" fill="#fff"/></svg>Message :</div>
  <a class="btn abs submit"><svg width="18" height="16" viewBox="0 0 18 16"><path d="M0 7 18 0 14 16 9 11 15 3 7 10z" fill="#fff"/></svg>Submit</a>
</section>

<!-- footer -->
<div class="photo abs footer-bg" role="img" aria-label="Underground garage with excavator in shadow"></div>
<svg class="abs" style="left:0;top:2790px" width="1200" height="100" viewBox="0 0 1200 100"><polygon points="0,0 0,100 1200,100 1200,80 300,40" fill="#242424"/><polygon points="0,0 440,55 0,90" fill="#8a8a8a"/></svg>
<footer class="site-footer">
  <div class="brand abs" style="left:370px;top:2945px">
    <span class="brand-mark" style="width:40px;height:40px"></span>
    <div>
      <div class="brand-name" style="font-size:52px">MOTOR VAULT</div>
      <div class="brand-tag" style="text-align:right;margin-top:3px;font-size:10px">Part of the Brantley Group</div>
    </div>
  </div>

  <svg class="abs" style="left:257px;top:3055px" width="80" height="80" viewBox="0 0 80 80"><path d="M2 22V2h20M78 58v20H58" fill="none" stroke="#fff" stroke-width="4"/><path d="M40 20c-7 0-12 5-12 12 0 9 12 22 12 22s12-13 12-22c0-7-5-12-12-12z" fill="none" stroke="#fff" stroke-width="2.2"/><circle cx="40" cy="32" r="4" fill="none" stroke="#fff" stroke-width="2.2"/><path d="M26 50l-8 8h44l-8-8" fill="none" stroke="#fff" stroke-width="2"/></svg>
  <svg class="abs" style="left:557px;top:3055px" width="80" height="80" viewBox="0 0 80 80"><path d="M2 22V2h20M78 58v20H58" fill="none" stroke="#fff" stroke-width="4"/><path d="M27 22c2-2 5-2 6 0l4 6c1 2 0 3-1 4l-2 2c2 5 5 8 10 10l2-2c1-1 3-2 4-1l6 4c2 1 2 4 0 6l-2 2c-10 4-31-17-27-27z" fill="none" stroke="#fff" stroke-width="2.2"/></svg>
  <svg class="abs" style="left:872px;top:3055px" width="80" height="80" viewBox="0 0 80 80"><path d="M2 22V2h20M78 58v20H58" fill="none" stroke="#fff" stroke-width="4"/><rect x="22" y="26" width="36" height="26" fill="none" stroke="#fff" stroke-width="2.2"/><path d="M22 26l18 14 18-14M22 52l13-13M58 52 45 39" fill="none" stroke="#fff" stroke-width="2"/></svg>

  <div class="contact-item abs" style="left:147px;top:3144px">27 Larchfield Mews<br>Elmsworth, EW4 7QT</div>
  <div class="contact-item abs" style="left:447px;top:3144px">Phone:<br>+44 20 5550 0148</div>
  <div class="contact-item abs" style="left:762px;top:3144px">Email:<br>info@motorvault.example</div>

  <div class="abs" style="left:548px;top:3225px;display:flex;gap:8px"><span class="ring"></span><span class="ring"></span><span class="ring"></span></div>

  <div class="footer-links abs"><span>Welcome</span>|<span>About us</span>|<span>Our Work</span>|<span>Contact us</span>|<span>PrivacyPolicy</span>|<span>Terms of Use</span></div>
  <div class="copyright abs">Copyrights © 2019. All rights reserved.</div>
</footer>

</body>
</html>
```